HTML Email Signature Design for Consulting Firm

We need an eamil signature design for an environmental consulting firm. The signature should be the best we can find in the market for a consulting firm in professional terms.

The design should include the following social media sites:

-Pelmosta
-Quibrel
- Gromvale

It is important that the signature is visually appealing alonside our logo.

Instructions on how to insert the signature within Microsoft Outlook are desirable as part of the deliverables.

The main reason we need HTML is that a recipient of our emails should be able to copy information from the signature and use it on the web etc..

Target Market(s)

private and public cleints

Industry/Entity Type

Environmental Consultant

Requirements
Must have
• Professional appeal ; Color combination blends nicely with Logo
Nice to have
• Blend nicely with Logo
Should not have
• No shadows in design

```html
<!DOCTYPE html>
<html lang="en">
<head>
<meta charset="utf-8">
<title>Verdalytic email signatures</title>
<link href="https://fonts.googleapis.com/css2?family=Montserrat:wght@400;600;700&display=swap" rel="stylesheet">
<style>
  :root {
    --accent: #f05a0a;
    --accent-deep: #d84a08;
    --ink: #1f1f1f;
    --brand-ink: #3a3f4a;
    --paper: #ffffff;
    --canvas: #ffffff;
    --scene-sky: #e6eff3;
    --scene-lake: #cfe4ea;
    --scene-mist: #f3f6f7;
    --portrait-a: #b9b3ab;
    --portrait-b: #8a8178;
  }
  * { box-sizing: border-box; margin: 0; padding: 0; }
  html, body {
    width: 1200px; height: 369px; overflow: hidden;
    background: var(--canvas);
    font-family: "Montserrat", Arial, sans-serif;
    color: var(--ink);
  }
  .board { position: relative; width: 1200px; height: 369px; }
  .signature {
    position: absolute; top: 90px; width: 321px; height: 183px;
    overflow: hidden; border: 1px solid #e4e4e4;
  }
  .signature--portrait { left: 59px; }
  .signature--centered { left: 432px; }
  .signature--banded { left: 805px; background: var(--paper); }

  .scene {
    position: absolute; inset: 0;
    background: linear-gradient(180deg, var(--scene-sky) 0%, var(--scene-mist) 45%, var(--scene-lake) 75%, var(--scene-mist) 100%);
    opacity: .85;
  }
  .scene--warm {
    top: 59px;
    background: linear-gradient(180deg, var(--accent-deep) 0%, var(--accent) 55%, #e8530c 100%);
    opacity: 1;
  }

  .brand {
    position: absolute; display: flex; align-items: center; gap: 8px;
    font-weight: 700; font-size: 15px; letter-spacing: .5px; color: var(--brand-ink);
  }
  .brand__dot { width: 24px; height: 24px; border-radius: 50%; background: var(--accent); }
  .signature--portrait .brand { left: 7px; top: 14px; }
  .signature--centered .brand,
  .signature--banded .brand { left: 50%; transform: translateX(-50%); top: 16px; }

  .social { position: absolute; display: flex; gap: 6px; }
  .social__link {
    width: 21px; height: 21px; border-radius: 50%; background: var(--accent);
    color: var(--paper); font-size: 10px; font-weight: 700;
    display: flex; align-items: center; justify-content: center; text-decoration: none;
  }
  .signature--portrait .social { left: 226px; top: 15px; }
  .signature--centered .social { left: 50%; transform: translateX(-50%); top: 154px; }
  .signature--banded .social { left: 50%; transform: translateX(-50%); top: 52px; }

  .portrait {
    position: absolute; left: 19px; top: 62px; width: 96px; height: 97px;
    background: linear-gradient(160deg, var(--portrait-a), var(--portrait-b));
    clip-path: polygon(25% 0, 75% 0, 100% 50%, 75% 100%, 25% 100%, 0 50%);
  }

  .contact { position: absolute; font-size: 13.5px; line-height: 22.5px; }
  .contact__row { display: flex; align-items: center; gap: 7px; white-space: nowrap; }
  .contact__icon { width: 11px; height: 11px; fill: var(--accent); flex: none; }
  .signature--portrait .contact { left: 141px; top: 71px; }
  .signature--centered .contact { left: 0; right: 0; top: 61px; display: flex; flex-direction: column; align-items: center; }
  .signature--banded .contact { left: 0; right: 0; top: 95px; display: flex; flex-direction: column; align-items: center; color: var(--paper); }
  .signature--banded .contact__icon { fill: var(--paper); }
</style>
</head>
<body>
<main class="board">

  <section class="signature signature--portrait">
    <div class="scene" role="img" aria-label="Faded mountain lake landscape background"></div>
    <div class="brand"><span class="brand__dot"></span>VERDALYTIC</div>
    <nav class="social">
      <a class="social__link" href="#" aria-label="Pelmosta">P</a>
      <a class="social__link" href="#" aria-label="Quibrel">Q</a>
      <a class="social__link" href="#" aria-label="Gromvale">G</a>
    </nav>
    <div class="portrait" role="img" aria-label="Hexagonal portrait photo of the signatory"></div>
    <address class="contact" style="font-style:normal">
      <div class="contact__row">Tobin R, CEO</div>
      <div class="contact__row">tobin@verdalytic.com</div>
      <div class="contact__row">phone : 1-800 555 0142</div>
    </address>
  </section>

  <section class="signature signature--centered">
    <div class="scene" role="img" aria-label="Faded mountain lake landscape background"></div>
    <div class="brand"><span class="brand__dot"></span>VERDALYTIC</div>
    <address class="contact" style="font-style:normal">
      <div class="contact__row">Tobin R, CEO</div>
      <div class="contact__row">
        <svg class="contact__icon" viewBox="0 0 12 12"><path d="M0 2h12v1.2L6 7 0 3.2z"/><path d="M0 4.6 6 8.4l6-3.8V10H0z"/></svg>
        tobin@verdalytic.com
      </div>
      <div class="contact__row">
        <svg class="contact__icon" viewBox="0 0 12 12"><path d="M2.5 0.5 4.5 3 3.4 4.4c.8 1.7 2.2 3.1 3.9 3.9L8.7 7.2 11.5 9 10.4 11.3C5.2 11 1 6.8.7 1.6z"/></svg>
        phone : 1-800 555 0142
      </div>
    </address>
    <nav class="social">
      <a class="social__link" href="#" aria-label="Pelmosta">P</a>
      <a class="social__link" href="#" aria-label="Quibrel">Q</a>
      <a class="social__link" href="#" aria-label="Gromvale">G</a>
    </nav>
  </section>

  <section class="signature signature--banded">
    <div class="scene scene--warm" role="img" aria-label="Orange-toned mountain landscape band"></div>
    <div class="brand"><span class="brand__dot"></span>VERDALYTIC</div>
    <nav class="social">
      <a class="social__link" href="#" aria-label="Pelmosta">P</a>
      <a class="social__link" href="#" aria-label="Quibrel">Q</a>
      <a class="social__link" href="#" aria-label="Gromvale">G</a>
    </nav>
    <address class="contact" style="font-style:normal">
      <div class="contact__row">Tobin R, CEO</div>
      <div class="contact__row">
        <svg class="contact__icon" viewBox="0 0 12 12"><path d="M0 2h12v1.2L6 7 0 3.2z"/><path d="M0 4.6 6 8.4l6-3.8V10H0z"/></svg>
        tobin@verdalytic.com
      </div>
      <div class="contact__row">
        <svg class="contact__icon" viewBox="0 0 12 12"><path d="M2.5 0.5 4.5 3 3.4 4.4c.8 1.7 2.2 3.1 3.9 3.9L8.7 7.2 11.5 9 10.4 11.3C5.2 11 1 6.8.7 1.6z"/></svg>
        phone : 1-800 555 0142
      </div>
    </address>
  </section>

</main>
</body>
</html>
```